Architectural, Engineering and Design Build

Tovantek4.com
Veteran Disabled Certified company is doing business in Architecture, Engineer and Design build - look simialr websites and come up with design follow following website
https://harlow-vessant.example/
https://www.quenforgroup.example/
https://www.ddelbmx.example/contract-vehicles/service-disabled-veteran-owned-small-business-sdvosb/
https://www.ostrelgrouplink.example/about/sdvosb/

Target Market(s)

US - Defense and Federal Government

Industry/Entity Type

Colors
0054AA
0677BA
7BADD7
CADEEF
E8F1F8

Requirements
Must have
• Army, American patriotism , Buildings, construction, architecture, engineering
Nice to have
• I need to attract federal government agencies and Defense

```html
<!DOCTYPE html>
<html lang="en">
<head>
<meta charset="utf-8">
<title>Tovantek4 — Service Disabled Veteran Owned Small Business</title>
<link rel="stylesheet" href="https://fonts.googleapis.com/css2?family=Oswald:wght@400;500;600&family=Lato:wght@400;700&display=swap">
<style>
:root{
  --navy:#1b2a6e;
  --navy-deep:#14205a;
  --red:#e1060d;
  --white:#ffffff;
  --ink:#1d1d1f;
  --text:#444a55;
  --muted:#7a7f88;
  --light:#f2f3f5;
  --line:#d8dbe0;
  --head:'Oswald',sans-serif;
  --body:'Lato',sans-serif;
}
*{box-sizing:border-box;margin:0;padding:0}
html,body{width:1200px;height:3171px;overflow:hidden}
body{position:relative;background:var(--white);font-family:var(--body);color:var(--text)}
.abs{position:absolute}
.head{font-family:var(--head);text-transform:uppercase;font-weight:500}
.btn{position:absolute;display:flex;align-items:center;justify-content:center;border-radius:24px;font-family:var(--head);font-weight:500;text-transform:uppercase;font-size:17px;box-shadow:0 4px 8px rgba(0,0,0,.18)}
.btn-red{background:var(--red);color:var(--white)}
.btn-white{background:var(--white);color:var(--red)}
.rule{position:absolute;height:2px;background:var(--line)}
.rule b{position:absolute;left:50%;top:-1px;width:38px;height:4px;background:var(--ink);transform:translateX(-50%)}

/* top bar */
.topbar{position:absolute;left:0;top:0;width:1200px;height:86px;background:var(--white)}
.mail-label{left:156px;top:22px;font-family:var(--head);font-size:12px;color:var(--red)}
.mail-value{left:156px;top:40px;font-family:var(--head);font-size:17px;color:var(--ink)}
.nav{position:absolute;left:0;top:86px;width:1200px;height:74px;background:var(--navy)}
.nav a{position:absolute;top:26px;font-family:var(--head);font-size:16px;color:var(--white);text-decoration:none;text-transform:uppercase}
.nav a.active{border-bottom:2px solid var(--white)}
.brand-ring{position:absolute;z-index:5;left:478px;top:78px;width:244px;height:126px;border-radius:0 0 122px 122px;background:rgba(255,255,255,.55)}
.brand-circle{position:absolute;z-index:6;left:502px;top:6px;width:196px;height:188px;border-radius:50%;background:var(--white);display:flex;align-items:center;justify-content:center;font-family:var(--head);font-weight:600;font-size:36px;color:var(--navy);letter-spacing:1px}

/* hero */
.hero{position:absolute;left:0;top:160px;width:1200px;height:505px;background:linear-gradient(160deg,#2a2b3a 0%,#6d4a3a 22%,#3b3f58 45%,#2c3350 70%,#1e2338 100%)}
.hero-title{position:absolute;width:1200px;text-align:center;color:var(--white)}
.arrow{position:absolute;width:28px;height:28px;border-radius:50%;display:flex;align-items:center;justify-content:center}
.arrow-soft{background:rgba(255,255,255,.45)}
.arrow-solid{background:var(--white)}
.arrow-navy{background:var(--navy)}
.arrow-grey{background:#b9bcc2}

/* certification */
.cert-card{left:111px;top:739px;width:431px;height:360px;background:var(--white);box-shadow:0 4px 22px rgba(0,0,0,.09)}
.cert-heading{left:622px;top:724px;width:540px;font-size:31px;line-height:47px;color:var(--navy);white-space:nowrap}
.para{font-size:15px;line-height:26px;color:var(--text)}

/* services */
.services-panel{left:0;top:1178px;width:542px;height:714px;background:var(--red)}
.services-photo{left:542px;top:1178px;width:658px;height:714px;background:linear-gradient(180deg,#e9edf1 0%,#f4f5f6 40%,#d9dde2 70%,#eef0f2 100%)}
.svc-title{position:absolute;left:174px;font-family:var(--head);font-size:19px;color:var(--white);text-transform:uppercase}
.svc-text{position:absolute;left:172px;width:335px;font-size:12.5px;line-height:22px;color:var(--white)}
.svc-icon{position:absolute;left:111px}
.svc-divider{position:absolute;left:111px;width:393px;height:1px;background:rgba(255,255,255,.7)}
.svc-highlight{left:0;top:1547px;width:542px;height:115px;background:linear-gradient(100deg,#1c2e78,#2d3f8e 60%,#22357f)}

/* testimonials */
.t-card{position:absolute;top:2048px;width:300px;height:202px;background:var(--white);box-shadow:0 3px 16px rgba(0,0,0,.09);border-radius:4px}
.t-avatar{position:absolute;left:9px;top:13px;width:64px;height:64px;border-radius:50%}
.t-stars{position:absolute;left:95px;top:12px;color:#f3a81c;font-size:12px;letter-spacing:1px}
.t-name{position:absolute;left:94px;top:26px;font-size:17px;font-weight:700;color:var(--ink)}
.t-date{position:absolute;left:95px;top:60px;font-size:10px;color:var(--muted)}
.t-text{position:absolute;left:12px;top:88px;width:280px;font-size:13.5px;line-height:26px;color:var(--text)}

/* contact */
.contact{left:0;top:2318px;width:1200px;height:540px;background:var(--light)}
.info-icon{position:absolute;left:113px;width:63px;height:63px;border-radius:50%;background:var(--navy);display:flex;align-items:center;justify-content:center}
.info-label{position:absolute;left:186px;font-family:var(--head);font-size:17px;color:var(--ink);text-transform:uppercase}
.info-value{position:absolute;left:187px;font-size:15.5px;line-height:28px;color:var(--ink)}
.field{position:absolute;background:var(--white);box-shadow:0 2px 8px rgba(0,0,0,.05);font-size:14px;color:#555;padding:0 17px;display:flex;align-items:center}
.field.msg{align-items:flex-start;padding-top:18px}

/* footer */
.footer{left:0;top:2858px;width:1200px;height:313px;background:var(--navy)}
.footer-mark{position:absolute;left:160px;top:2922px;width:248px;height:166px;display:flex;align-items:center;gap:10px}
.footer-dot{width:22px;height:22px;border-radius:50%;background:var(--white)}
.footer-name{font-family:var(--head);font-weight:600;font-size:40px;color:var(--white);letter-spacing:1px}
.footer-links a{position:absolute;top:2936px;font-size:15px;color:var(--white);text-decoration:none;text-transform:uppercase}
.footer-line{position:absolute;left:506px;font-size:15px;color:var(--white);text-transform:uppercase}
.social{position:absolute;top:3078px;width:25px;height:25px;border-radius:50%;background:var(--white)}
.social.accent{background:var(--red);border:2px solid var(--white)}
</style>
</head>
<body>

<!-- top bar -->
<header class="topbar">
  <svg class="abs" style="left:110px;top:24px" width="36" height="36" viewBox="0 0 36 36" fill="none" stroke="#e1060d" stroke-width="1.6"><path d="M4 14 L18 4 L32 14 V32 H4 Z"/><path d="M4 14 L18 24 L32 14"/><circle cx="18" cy="14" r="4"/></svg>
  <div class="abs head mail-label">Send us email</div>
  <div class="abs mail-value">INFO@TOVANTEK4.COM</div>
  <div class="btn btn-red" style="left:942px;top:21px;width:146px;height:42px;box-shadow:none">Request a quote</div>
</header>

<nav class="nav">
  <a class="active" style="left:111px">Home</a>
  <a style="left:206px">About</a>
  <a style="left:308px">Services</a>
  <a style="left:817px">Blog</a>
  <a style="left:903px">Careers</a>
  <a style="left:1013px">Contact us</a>
</nav>

<!-- hero -->
<section class="hero" role="img" aria-label="Sunset sky with a waving American flag"></section>
<div class="hero-title head" style="top:280px;font-size:26px">Welcome to Tovantek4</div>
<div class="hero-title head" style="top:326px;font-size:48px;letter-spacing:.3px">Service Disabled Veteran Owned Small Business</div>
<p class="hero-title" style="top:400px;font-size:15px;line-height:29px">Itaque earum rerum hic tenetur a sapiente delectus, ut aut reiciendis voluptatibus maiores alias<br>consequatur aut perferendis doloribus asperiores repellat.</p>
<div class="btn btn-white" style="left:528px;top:484px;width:145px;height:46px">Get started</div>
<div class="arrow arrow-soft" style="left:45px;top:395px"><svg width="12" height="12" viewBox="0 0 12 12"><path d="M8 1 L3 6 L8 11" stroke="#555" stroke-width="2" fill="none"/></svg></div>
<div class="arrow arrow-solid" style="left:1126px;top:395px"><svg width="12" height="12" viewBox="0 0 12 12"><path d="M4 1 L9 6 L4 11" stroke="#111" stroke-width="2" fill="none"/></svg></div>

<!-- brand mark -->
<div class="brand-ring"></div>
<div class="brand-circle">TOVANTEK4</div>

<!-- certification -->
<div class="abs cert-card">
  <div class="abs" style="left:70px;top:40px;width:290px;height:270px;border-radius:50%;background:#eef1f8;border:14px solid #2c55a6" role="img" aria-label="Certification badge"></div>
</div>
<h2 class="abs head cert-heading">Certification for Service Disabled<br>Veteran Owned Small Business</h2>
<div class="abs" style="left:623px;top:833px;width:38px;height:4px;background:var(--ink)"></div>
<div class="abs" style="left:661px;top:834px;width:14px;height:2px;background:var(--line)"></div>
<p class="abs para" style="left:623px;top:856px;width:470px">Nam libero tempore, cum soluta nobis est eligendi optio cumque nihil nda est, omnis dolor repellendus. Temporibus autem quibusdam et rerum necessitatibus saepe eveniet ut et voluptates repudiandae sint et molestiae non recusandae.</p>
<p class="abs para" style="left:623px;top:985px;width:470px">Itaque earum rerum hic tenetur a sapiente delectus, ut aut reiciendis equatur aut perferendis doloribus asperiores repellat.</p>
<div class="btn btn-red" style="left:623px;top:1056px;width:145px;height:47px">Read more</div>

<!-- services -->
<section class="abs services-panel"></section>
<div class="abs services-photo" role="img" aria-label="Modern white building over architectural blueprints"></div>
<div class="abs svc-highlight" role="img" aria-label="Faded American flag background"></div>
<h2 class="abs head" style="left:111px;top:1228px;font-size:33px;color:var(--white)">Our Services</h2>
<div class="abs" style="left:111px;top:1292px;width:38px;height:4px;background:var(--white)"></div>
<div class="abs" style="left:149px;top:1294px;width:46px;height:1px;background:var(--white)"></div>

<svg class="svc-icon" style="top:1348px" width="34" height="40" viewBox="0 0 34 40" fill="none" stroke="#fff" stroke-width="1.5"><rect x="3" y="12" width="12" height="26"/><rect x="15" y="4" width="16" height="34"/><path d="M19 10h3M25 10h3M19 17h3M25 17h3M19 24h3M25 24h3M6 18h6M6 25h6M1 38h32"/></svg>
<div class="svc-title" style="top:1326px">Buildings</div>
<p class="svc-text" style="top:1360px">Itaque earum rerum hic tenetur a sapiente delectus, ut aut s aut perferendis doloribus asperiores repellat.</p>
<div class="svc-divider" style="top:1430px"></div>

<svg class="svc-icon" style="top:1472px" width="38" height="42" viewBox="0 0 38 42" fill="none" stroke="#fff" stroke-width="1.5"><path d="M8 40V6M2 8h30M8 6l-5 4M26 8v8"/><rect x="20" y="24" width="16" height="16"/><path d="M24 29h3M30 29h3M24 34h3M30 34h3M1 40h36"/></svg>
<div class="svc-title" style="top:1450px">Construction</div>
<p class="svc-text" style="top:1484px">Itaque earum rerum hic tenetur a sapiente delectus, ut aut s aut perferendis doloribus asperiores repellat.</p>

<svg class="svc-icon" style="top:1588px" width="40" height="38" viewBox="0 0 40 38" fill="none" stroke="#fff" stroke-width="1.5"><rect x="2" y="10" width="30" height="26"/><path d="M8 30V22l8-6 8 6v8M6 30h22M24 4l12 12-14 14"/></svg>
<div class="svc-title" style="top:1565px">Architecture</div>
<p class="svc-text" style="top:1599px;font-weight:700">Taque earum rerum hic tenetur a sapiente delectus, ut aut s aut perferendis doloribus asperiores repellat.</p>

<svg class="svc-icon" style="top:1706px" width="38" height="40" viewBox="0 0 38 40" fill="none" stroke="#fff" stroke-width="1.5"><circle cx="15" cy="12" r="8"/><path d="M7 10h16M3 38c0-10 6-14 12-14s12 4 12 14"/><circle cx="29" cy="9" r="5"/><path d="M29 2v3M29 13v3M22 9h3M33 9h3"/></svg>
<div class="svc-title" style="top:1683px">Engineering</div>
<p class="svc-text" style="top:1717px">Itaque earum rerum hic tenetur a sapiente delectus, ut aut s aut perferendis doloribus asperiores repellat.</p>
<div class="btn btn-white" style="left:110px;top:1790px;width:145px;height:47px">View more</div>

<!-- testimonials -->
<h2 class="abs head" style="left:0;top:1942px;width:1200px;text-align:center;font-size:33px;color:var(--navy)">What Customer Says</h2>
<div class="rule" style="left:547px;top:2007px;width:106px"><b></b></div>

<article class="t-card" style="left:111px">
  <div class="t-avatar" style="background:#c9a48d" role="img" aria-label="Customer portrait"></div>
  <div class="t-stars">★★★★★</div>
  <div class="t-name">Daniel Corvane</div>
  <div class="t-date">April 12, 2024</div>
  <p class="t-text">Temporibus autem quibusdam et aut officiis debitis aut rerum necessitatibus saepe eveniet ut et voluptates nt et moles tiae non recusandae.</p>
</article>
<article class="t-card" style="left:448px">
  <div class="t-avatar" style="background:#6f7c8a" role="img" aria-label="Customer portrait"></div>
  <div class="t-stars">★★★★★</div>
  <div class="t-name">Marcus Pellin</div>
  <div class="t-date">June 12, 2023</div>
  <p class="t-text" style="color:var(--ink)">Itaque earum rerum hic tenetur a sapiente delectus, ut aut reiciendis voluptatibus maiores alias consequatur aut perferendis doloribus asperiores repellat.</p>
</article>
<article class="t-card" style="left:788px">
  <div class="t-avatar" style="background:#a88068" role="img" aria-label="Customer portrait"></div>
  <div class="t-stars">★★★★★</div>
  <div class="t-name">Laura Whitfen</div>
  <div class="t-date">April 24, 2024</div>
  <p class="t-text">Nam libero tempore, cum soluta nobis est eligendi optio cumque nihil impedit quo minus id quod maxime placeat facere maxime placea possimus.</p>
</article>
<div class="arrow arrow-grey" style="left:45px;top:2139px"><svg width="12" height="12" viewBox="0 0 12 12"><path d="M8 1 L3 6 L8 11" stroke="#fff" stroke-width="2" fill="none"/></svg></div>
<div class="arrow arrow-navy" style="left:1126px;top:2139px"><svg width="12" height="12" viewBox="0 0 12 12"><path d="M4 1 L9 6 L4 11" stroke="#fff" stroke-width="2" fill="none"/></svg></div>

<!-- contact -->
<section class="abs contact"></section>
<div class="abs" style="left:1104px;top:2318px;width:92px;height:100px;background:rgba(225,6,13,.12)" role="img" aria-label="Red dot pattern decoration"></div>
<h2 class="abs head" style="left:0;top:2365px;width:1200px;text-align:center;font-size:33px;color:var(--navy)">Get in Touch With Us</h2>
<div class="rule" style="left:546px;top:2430px;width:106px"><b></b></div>

<div class="info-icon" style="top:2476px"><svg width="18" height="24" viewBox="0 0 18 24"><path d="M9 0C4 0 0 4 0 9c0 7 9 15 9 15s9-8 9-15c0-5-4-9-9-9z" fill="#fff"/><circle cx="9" cy="9" r="3.2" fill="#1b2a6e"/></svg></div>
<div class="info-label" style="top:2468px">Location</div>
<div class="info-value" style="top:2497px">Tovantek4<br>United States</div>

<div class="info-icon" style="top:2601px"><svg width="22" height="22" viewBox="0 0 24 24"><path d="M6.6 10.8a15 15 0 0 0 6.6 6.6l2.2-2.2c.3-.3.7-.4 1-.2 1.1.4 2.3.6 3.6.6.6 0 1 .4 1 1V20c0 .6-.4 1-1 1C10.6 21 3 13.4 3 4c0-.6.4-1 1-1h3.5c.6 0 1 .4 1 1 0 1.3.2 2.5.6 3.6.1.3 0 .7-.2 1z" fill="#fff"/></svg></div>
<div class="info-label" style="top:2604px">Phone number</div>
<div class="info-value" style="top:2633px">+1 888 888 8888</div>

<div class="info-icon" style="top:2716px"><svg width="22" height="16" viewBox="0 0 22 16"><rect width="22" height="16" rx="2" fill="#fff"/><path d="M1 2l10 7 10-7" stroke="#1b2a6e" stroke-width="1.8" fill="none"/></svg></div>
<div class="info-label" style="top:2718px">Email address</div>
<div class="info-value" style="top:2747px">info@tovantek4.com</div>

<div class="field" style="left:511px;top:2477px;width:283px;height:49px">Name</div>
<div class="field" style="left:805px;top:2477px;width:283px;height:49px">Your Email</div>
<div class="field" style="left:511px;top:2540px;width:283px;height:49px">Your Phone</div>
<div class="field" style="left:805px;top:2540px;width:283px;height:49px;justify-content:space-between">Services<svg width="10" height="6" viewBox="0 0 10 6"><path d="M0 0h10L5 6z" fill="#222"/></svg></div>
<div class="field msg" style="left:511px;top:2604px;width:577px;height:110px">Message</div>
<div class="btn btn-red" style="left:512px;top:2740px;width:144px;height:47px">Submit</div>

<!-- footer -->
<footer class="abs footer"></footer>
<div class="footer-mark"><span class="footer-dot"></span><span class="footer-name">TOVANTEK4</span></div>
<div class="footer-links">
  <a style="left:506px">Home</a>
  <a style="left:582px">About</a>
  <a style="left:666px">Services</a>
  <a style="left:767px">Careers</a>
  <a style="left:865px">News</a>
  <a style="left:938px">Contact us</a>
</div>
<div class="footer-line" style="top:2984px">Mail us: info@tovantek4.com &nbsp;&nbsp;&nbsp;&nbsp;&nbsp;| &nbsp;&nbsp;&nbsp;&nbsp;&nbsp;Call us: +1 888 888 8888</div>
<div class="footer-line" style="top:3032px">Copyrights@2024.Tovantek4.All rights reserved</div>
<span class="social accent" style="left:507px"></span>
<span class="social" style="left:557px"></span>
<span class="social" style="left:606px"></span>
<span class="social" style="left:656px"></span>

</body>
</html>
```